Visitenkarten-Design
Zielgruppe
Malerbetrieb
Zielgruppe: Private Haushalte, Hausverwaltungen
Aufgabenstellung
Logo ist vorhanden
Lorenz Dallmer
Malermeister

```html
<!DOCTYPE html>
<html lang="de">
<head>
<meta charset="utf-8">
<title>Visitenkarte – Malereibetrieb Dallmer</title>
<link rel="stylesheet" href="https://fonts.googleapis.com/css2?family=Inter:wght@400;600&display=swap">
<style>
  :root {
    --backdrop: #e4e4e4;
    --card: #f4f4f3;
    --ink: #1b1d22;
    --ink-soft: #6b6d70;
    --cyan: #00a2e3;
    --yellow: #f7dd00;
    --magenta: #d1006f;
  }
  * { margin: 0; padding: 0; box-sizing: border-box; }
  html, body {
    width: 1200px;
    height: 900px;
    overflow: hidden;
    background: var(--backdrop);
    font-family: "Inter", "Helvetica Neue", Arial, sans-serif;
    color: var(--ink);
  }
  .business-card {
    position: absolute;
    left: 100px;
    top: 165px;
    width: 1000px;
    height: 571px;
    background: var(--card);
    box-shadow: 0 2px 6px rgba(0,0,0,0.12);
  }
  .colour-mark {
    position: absolute;
    left: 0;
    height: 67px;
  }
  .colour-mark--cyan { top: 244px; width: 53px; background: var(--cyan); }
  .colour-mark--yellow { top: 349px; width: 35px; background: var(--yellow); }
  .colour-mark--magenta { top: 453px; width: 53px; background: var(--magenta); }

  .brand {
    position: absolute;
    right: 49px;
    top: 52px;
    text-align: right;
  }
  .brand-name {
    display: flex;
    align-items: center;
    justify-content: flex-end;
    gap: 10px;
    font-weight: 600;
    font-size: 30px;
    line-height: 1;
    color: var(--ink);
    letter-spacing: 0.01em;
  }
  .brand-square {
    width: 22px;
    height: 22px;
    background: var(--cyan);
  }
  .brand-slogan {
    margin-top: 8px;
    font-size: 14px;
    color: var(--ink-soft);
  }

  .contact {
    position: absolute;
    left: 83px;
    font-size: 28px;
    line-height: 1;
    color: var(--ink);
  }
  .person-name { top: 237px; font-size: 34px; font-weight: 600; }
  .person-role { top: 294px; }
  .address { top: 352px; }
  .phone { top: 396px; }
  .email { top: 456px; }
  .website { top: 501px; }
</style>
</head>
<body>
  <main class="business-card">
    <div class="colour-mark colour-mark--cyan"></div>
    <div class="colour-mark colour-mark--yellow"></div>
    <div class="colour-mark colour-mark--magenta"></div>

    <div class="brand">
      <div class="brand-name"><span class="brand-square"></span>Dallmer Malereibetrieb</div>
      <p class="brand-slogan">Sorgfalt in jeder Farbschicht</p>
    </div>

    <p class="contact person-name">Lorenz Dallmer</p>
    <p class="contact person-role">Malermeister</p>
    <p class="contact address">Lindenkamp 48 b | 22147 Hamburg</p>
    <p class="contact phone">Tel: 0172- 5 418 230</p>
    <p class="contact email">info@malereibetrieb-dallmer.de</p>
    <p class="contact website">www.malereibetrieb-dallmer.de</p>
  </main>
</body>
</html>
```